Torvane Template Design for Pressmoor Quillpath Site

We need graphic design and theme design work for our new site that will be running Quillpath with Torvane as the theme.

We have a draft logo that needs a graphic designer to improve it.

We are looking for sleek, modern, design that while minimal is distinct. ie page elements, content enhancement, block design that can be used, reused by in-house team.
This means there will also need to be a guide created on how to create, insert, edit each of those elements so that they can be used on new pages over time.

We have several businesses for which this is the "umbrella company" and so we will want to unify the colours and have identified a palette from which to start.

Some examples of site design we would like to stand up like:
https://www.zlt-example.com/
https://latchpromo-example.com/
https://business.veltrix-example.com/
https://www.norvask-example.com/learning/home.aspx

When I say "coded" below, this really just means the CSS needed for page elements.

Target Market(s)

Small firms in professional services - engineers, land surveyors, consultants

Number of Pages Required

3 page

Font styles to use
Sans Serif

Requirements
Must have
• Pressmoor/Torvane as base template, full home page layout with lorem ipsum placeholder
Nice to have
• custom blocks for pull quotes, call to action, a better design on the logo so it doesn't look like a rainbow.
Should not have
• Need for Blockwright

```html
<!DOCTYPE html>
<html lang="en">
<head>
<meta charset="utf-8">
<title>Corvella – Branding for Professional Services Firms</title>
<link href="https://fonts.googleapis.com/css2?family=Oswald:wght@400;500;600&family=Roboto:wght@400;500;700&display=swap" rel="stylesheet">
<style>
:root{
  --teal:#0aa6bf;
  --yellow:#fdb913;
  --green:#6aae4c;
  --purple:#563e8f;
  --navy:#333f7d;
  --ink:#222222;
  --body:#555555;
  --muted:#888888;
  --soft:#f2f2f2;
  --line:#e6e6e6;
  --white:#ffffff;
}
*{box-sizing:border-box;margin:0;padding:0}
html,body{width:1200px;height:3812px;overflow:hidden}
body{font-family:"Roboto",Arial,sans-serif;color:var(--body);background:var(--white);position:relative}
.head-font{font-family:"Oswald","Arial Narrow",sans-serif;color:var(--ink);font-weight:500}
p{font-size:11.5px;line-height:20px}
.btn{position:absolute;display:flex;align-items:center;justify-content:center;gap:5px;font-size:11.5px;font-weight:500;text-transform:uppercase;letter-spacing:.2px}
.btn-yellow{background:var(--yellow);color:#2a2a2a}
.btn .dot{width:10px;height:10px;border-radius:50%;background:currentColor;display:inline-flex;align-items:center;justify-content:center}
.btn .dot svg{width:6px;height:6px}
.eyebrow{display:flex;align-items:center;gap:10px;font-size:14px;text-transform:uppercase}
.eyebrow::before{content:"";width:22px;height:3px;background:var(--yellow)}
.ticks{list-style:none}
.ticks li{font-size:11.5px;line-height:23px;padding-left:16px;position:relative;white-space:nowrap}
.ticks li::before{content:"";position:absolute;left:0;top:8px;width:7px;height:7px;border-radius:50%;border:1px solid currentColor}
.ph{position:absolute}

/* header */
.site-header{position:absolute;left:0;top:0;width:1200px;height:71px;background:var(--white)}
.brand{position:absolute;left:108px;top:12px;font-family:"Oswald",sans-serif;font-size:32px;font-weight:400;color:var(--ink);letter-spacing:-.5px}
.nav{position:absolute;left:671px;top:29px;display:flex;gap:19px;font-size:12px;font-weight:500;color:#444}
.btn-green{background:var(--green);color:#fff;left:909px;top:14px;width:184px;height:41px;font-size:12px}

/* hero */
.hero{position:absolute;left:0;top:71px;width:1200px;height:554px;background:linear-gradient(100deg,#d7d6d0 0%,#cfcfc8 30%,#4d5a5f 48%,#8b9a3f 62%,#5c6c74 78%,#3d4a58 100%)}
.hero-fade{position:absolute;left:0;top:0;width:560px;height:554px;background:rgba(255,255,255,.55)}
.hero-card{position:absolute;left:108px;top:71px;width:570px;height:411px;background:var(--white)}
.hero-card .eyebrow{position:absolute;left:54px;top:74px;color:#777}
.hero-card h1{position:absolute;left:54px;top:103px;font-size:29px;line-height:33px;font-weight:500;text-transform:uppercase;letter-spacing:-.6px;width:480px}
.hero-card p{position:absolute;left:54px;top:184px;width:468px;font-size:11px;line-height:20px}
.btn-teal{background:var(--teal);color:#fff;left:56px;top:281px;width:157px;height:47px}
.hero-call{position:absolute;left:230px;top:297px;font-size:13.5px;font-weight:500;color:var(--ink)}

/* services */
.services{position:absolute;left:0;top:625px;width:1200px;height:370px;background:var(--white)}
.services h2{position:absolute;left:108px;top:53px;font-size:27px;line-height:35px}
.services .intro{position:absolute;left:108px;top:131px;width:215px;font-size:11px;line-height:18px}
.services .btn-yellow{left:108px;top:228px;width:133px;height:41px}
.svc-card{position:absolute;top:57px;width:221px;height:242px;border:1px solid var(--line)}
.svc-icon{position:absolute;left:22px;top:30px;width:52px;height:52px;border-radius:50%;background:var(--yellow);display:flex;align-items:center;justify-content:center}
.svc-card h3{position:absolute;left:24px;top:94px;font-size:17px}
.svc-card p{position:absolute;left:24px;top:126px;width:178px;font-size:11px;line-height:19px}

/* about */
.about{position:absolute;left:0;top:995px;width:1200px;height:515px;background:var(--purple);color:#fff}
.about .exp{position:absolute;left:396px;top:53px;width:255px;height:212px;background:var(--teal);padding:22px 27px}
.exp .num{font-size:44px;font-weight:500;line-height:50px}
.exp .lbl{font-size:17px;font-weight:500;margin:2px 0 8px}
.exp p{font-size:11px;line-height:19px}
.about .eyebrow{position:absolute;left:715px;top:66px;font-size:17px;font-weight:500;color:#fff}
.about h2{position:absolute;left:713px;top:78px;font-size:68px;line-height:90px;color:#fff;font-weight:600}
.about .text{position:absolute;left:715px;top:172px;width:380px;font-size:11px;line-height:19.5px}
.about .ticks{position:absolute;left:715px;top:284px;color:#fff}
.about .ticks li{font-size:11px}
.about .btn-yellow{left:719px;top:394px;width:132px;height:43px}

/* why */
.why{position:absolute;left:0;top:1510px;width:1200px;height:310px;background:var(--soft)}
.why h2{position:absolute;left:0;top:60px;width:1200px;text-align:center;font-size:43px;font-weight:500}
.why-item{position:absolute;top:165px;display:flex;gap:20px}
.why-icon{width:66px;height:66px;border-radius:50%;background:var(--yellow);display:flex;align-items:center;justify-content:center;flex:none}
.why-item h3{font-size:17px;margin-top:2px}
.why-item p{font-size:11px;line-height:19px;margin-top:6px;width:180px}

/* solution */
.solution{position:absolute;left:0;top:1820px;width:1200px;height:500px;background:var(--white)}
.solution h2{position:absolute;left:688px;top:40px;width:420px;font-size:50px;line-height:57px;font-weight:500;letter-spacing:-.3px;white-space:nowrap}
.solution h2 .accent{color:var(--teal)}
.solution .text{position:absolute;left:690px;top:222px;width:405px;font-size:11px;line-height:20px}
.solution .ticks{position:absolute;left:690px;top:311px}
.solution .ticks li{font-size:11px}
.solution .ticks li::before{border-color:var(--teal)}
.solution .btn-yellow{left:691px;top:406px;width:155px;height:42px}

/* testimonials */
.testimonials{position:absolute;left:0;top:2320px;width:1200px;height:573px;background:var(--soft)}
.testimonials h2{position:absolute;left:0;top:66px;width:1213px;text-align:center;font-size:43px;font-weight:500}
.t-card{position:absolute;top:191px;width:312px;height:297px;background:var(--white)}
.t-badge{position:absolute;left:37px;top:-37px;width:48px;height:46px;background:var(--yellow);display:flex;align-items:center;justify-content:center}
.t-card p{position:absolute;left:38px;top:52px;width:240px;font-size:11px;line-height:20.5px;color:#444}
.t-card p::before{content:"\201C";position:absolute;left:-22px;top:-8px;font-size:30px;color:#ccc;font-family:Georgia,serif}
.t-avatar{position:absolute;left:39px;top:210px;width:58px;height:48px}
.t-name{position:absolute;left:112px;top:219px;font-size:11.5px;font-weight:500;color:#333}
.t-place{position:absolute;left:112px;top:236px;font-size:11px;color:var(--muted)}

/* faq */
.faq{position:absolute;left:0;top:2893px;width:1200px;height:450px;background:var(--white)}
.faq .eyebrow{position:absolute;left:108px;top:66px;color:#777;font-size:13px}
.faq h2{position:absolute;left:108px;top:102px;font-size:48px;line-height:52px;font-weight:500;letter-spacing:-.3px}
.faq .text{position:absolute;left:108px;top:233px;width:410px;font-size:11px;line-height:20px}
.faq .btn-yellow{left:108px;top:339px;width:124px;height:36px}
.faq-list{position:absolute;left:638px;top:94px;width:455px}
.faq-item{height:48px;margin-bottom:12px;background:#f4f4f4;display:flex;align-items:center;justify-content:space-between;padding:0 22px;font-size:11px;color:#333}
.faq-item b{font-size:18px;font-weight:400;color:#222}

/* partners */
.partners{position:absolute;left:0;top:3343px;width:1200px;height:149px;background:var(--white)}
.partner{position:absolute;top:62px;display:flex;align-items:center;gap:7px;font-weight:700;font-size:15px;color:#4a4a4a}
.partner i{display:block;width:14px;height:14px;border-radius:50%;background:#4a4a4a}
.seal{position:absolute;left:1036px;top:45px;width:54px;height:54px;border-radius:50%;border:3px solid #555}

/* footer */
.site-footer{position:absolute;left:0;top:3492px;width:1200px;height:320px;background:var(--navy);color:#fff}
.foot-brand{position:absolute;left:108px;top:58px;font-family:"Oswald",sans-serif;font-size:58px;font-weight:400;color:#fff}
.foot-phone-icon{position:absolute;left:484px;top:83px;width:52px;height:52px;border-radius:50%;background:var(--yellow);display:flex;align-items:center;justify-content:center}
.foot-ask{position:absolute;left:552px;top:92px;font-size:12px}
.foot-num{position:absolute;left:552px;top:110px;font-size:25px;font-weight:700}
.site-footer .btn-yellow{left:939px;top:109px;width:154px;height:41px}
.foot-rule{position:absolute;left:0;top:250px;width:1200px;height:1px;background:rgba(255,255,255,.18)}
.copyright{position:absolute;left:108px;top:274px;font-size:12px}
.socials{position:absolute;left:958px;top:267px;display:flex;gap:7px}
.socials span{width:28px;height:28px;border-radius:50%;border:1px solid #fff}
</style>
</head>
<body>

<header class="site-header">
  <div class="brand">Corvella</div>
  <nav class="nav"><span>ENGINEERS</span><span>LAND SURVEYORS</span></nav>
  <a class="btn btn-green">Get Free Consultants</a>
</header>

<section class="hero">
  <div class="ph" style="left:0;top:0;width:1200px;height:554px" role="img" aria-label="Photo of two engineers in hard hats and high-visibility jackets reviewing a laptop on site, with a surveyor at left"></div>
  <div class="hero-fade"></div>
  <div class="hero-card">
    <div class="eyebrow">23 Years of Experience</div>
    <h1 class="head-font">Research-Based Branding &amp; Marketing for Professional Services Firms</h1>
    <p>Lorem Ipsum is simply dummy text of the printing and typesetting industry lorem Ipsum has been the industry's standard dummy text ever since when an unknown printer took galley type and scrambled make &nbsp;type specimen book.</p>
    <a class="btn btn-teal">Our Services <span class="dot"><svg viewBox="0 0 6 6"><path d="M2 1l2 2-2 2" stroke="#0aa6bf" stroke-width="1.2" fill="none"/></svg></span></a>
    <div class="hero-call">OR &nbsp;&nbsp;CALL (123) 555-0147</div>
  </div>
</section>

<section class="services">
  <h2 class="head-font">Most Popular<br>Services</h2>
  <p class="intro">Lorem Ipsum is simply dummy textthe printing and typesetting industry lorem Ipsum has been the industry's standard scrambled make &nbsp;type specimen book.</p>
  <a class="btn btn-yellow">All Services</a>

  <div class="svc-card" style="left:384px">
    <div class="svc-icon"><svg width="28" height="28" viewBox="0 0 28 28" fill="none" stroke="#333" stroke-width="1.6"><path d="M7 12a7 7 0 0 1 14 0z"/><path d="M5 12h18"/><circle cx="14" cy="16" r="3"/><path d="M7 26c0-4 3-6 7-6s7 2 7 6"/></svg></div>
    <h3 class="head-font">Engineers</h3>
    <p>Lorem Ipsum is simply dummy textthe printing and typesetting industry lorem Ipsum has been scrambled make &nbsp;type specimen</p>
  </div>
  <div class="svc-card" style="left:627px">
    <div class="svc-icon"><svg width="28" height="28" viewBox="0 0 28 28" fill="none" stroke="#333" stroke-width="1.6"><rect x="6" y="4" width="16" height="20"/><path d="M10 9h8M10 14h8M10 19h5"/></svg></div>
    <h3 class="head-font">Land surveyors</h3>
    <p>Lorem Ipsum is simply dummy textthe printing and typesetting industry lorem Ipsum has been scrambled make &nbsp;type specimen</p>
  </div>
  <div class="svc-card" style="left:870px">
    <div class="svc-icon"><svg width="28" height="28" viewBox="0 0 28 28" fill="none" stroke="#333" stroke-width="1.6"><rect x="5" y="5" width="18" height="12"/><path d="M9 25v-4h10v4M14 17v4"/></svg></div>
    <h3 class="head-font">Consultants</h3>
    <p>Lorem Ipsum is simply dummy textthe printing and typesetting industry lorem Ipsum has been scrambled make &nbsp;type specimen</p>
  </div>
</section>

<section class="about">
  <div class="ph" style="left:108px;top:53px;width:268px;height:407px;background:linear-gradient(160deg,#9aa3aa,#5a5f63 55%,#c5672e)" role="img" aria-label="Photo of a surveyor in a white hard hat using a tripod instrument"></div>
  <div class="exp">
    <div class="num">23+</div>
    <div class="lbl">Years Of Experience</div>
    <p>Lorem Ipsum is simply dummy text industry. Lorem Ipsum has been the transfer sheets containing Lorem Ipsum passages, and more recently</p>
  </div>
  <div class="ph" style="left:396px;top:282px;width:255px;height:178px;background:linear-gradient(180deg,#8a9196,#5d6266 50%,#c7c2b8)" role="img" aria-label="Photo of a team meeting around a conference table"></div>
  <div class="eyebrow">Welcome to</div>
  <h2 class="head-font">CORVELLA</h2>
  <p class="text">Lorem Ipsum is simply dummy text of the printing and typesetting industry. Lorem Ipsum has been the industry's standard dummy text remaining essentially unchanged. It was popularised in the 1960s with the release of transfer sheets containing Lorem Ipsum passages, and more recently with desktop publishing software like Lorem Press</p>
  <ul class="ticks">
    <li>Lorem Ipsum is simply dummy text the printing and typesetting</li>
    <li>the release of transfer sheets containing Lorem Ipsum passages,</li>
    <li>more recently with desktop publishing software Lorem Press</li>
    <li>more recently with desktop publishing software Lorem Press</li>
  </ul>
  <a class="btn btn-yellow">Read More <span class="dot"><svg viewBox="0 0 6 6"><path d="M2 1l2 2-2 2" stroke="#fdb913" stroke-width="1.2" fill="none"/></svg></span></a>
</section>

<section class="why">
  <h2 class="head-font">WHY CHOOSE US</h2>
  <div class="why-item" style="left:110px">
    <div class="why-icon"><svg width="36" height="36" viewBox="0 0 36 36" fill="none" stroke="#333" stroke-width="1.8"><circle cx="18" cy="12" r="5"/><circle cx="8" cy="16" r="3.5"/><circle cx="28" cy="16" r="3.5"/><path d="M9 30c0-5 4-9 9-9s9 4 9 9M2 28c0-4 3-6 6-6M34 28c0-4-3-6-6-6"/></svg></div>
    <div><h3 class="head-font">Expert Team</h3><p>Lorem Ipsum is simply dummy scrambled make type specimen</p></div>
  </div>
  <div class="why-item" style="left:475px">
    <div class="why-icon"><svg width="36" height="36" viewBox="0 0 36 36" fill="none" stroke="#333" stroke-width="1.8"><path d="M18 6l13 7-13 7-13-7z"/><path d="M5 19l13 7 13-7M5 25l13 7 13-7"/></svg></div>
    <div><h3 class="head-font">Quality Materials</h3><p>Lorem Ipsum is simply dummy scrambled make type specimen</p></div>
  </div>
  <div class="why-item" style="left:837px">
    <div class="why-icon"><svg width="36" height="36" viewBox="0 0 36 36" fill="none" stroke="#333" stroke-width="1.8"><path d="M8 4h15l6 6v22H8z"/><path d="M12 14h12M12 19h12M12 24h7"/><circle cx="26" cy="27" r="4"/></svg></div>
    <div><h3 class="head-font">Details Proposal</h3><p>Lorem Ipsum is simply dummy scrambled make type specimen</p></div>
  </div>
</section>

<section class="solution">
  <div class="ph" style="left:0;top:0;width:623px;height:500px;background:linear-gradient(120deg,#dfe6ee,#b9c7d6 45%,#e9eef3 70%,#5b6f8a)" role="img" aria-label="Photo of a businesswoman presenting charts on a large screen to colleagues"></div>
  <h2 class="head-font">A solution that feels<br>made for you —<br><span class="accent">because it was</span></h2>
  <p class="text">Lorem Ipsum is simply dummy text of the printing and typesetting industry lorem Ipsum has been the industry's standard dummy text ever since when centuries, but also the leap into electronic typesetting, remaining essentially sheets containing Lorem Ipsum passages, and more recently with desktop</p>
  <ul class="ticks">
    <li>Lorem Ipsum is simply dummy text the printing and typesetting</li>
    <li>the release of transfer sheets containing Lorem Ipsum passages,</li>
    <li>more recently with desktop publishing software Lorem Press</li>
  </ul>
  <a class="btn btn-yellow">Get Consultant <span class="dot"><svg viewBox="0 0 6 6"><path d="M2 1l2 2-2 2" stroke="#fdb913" stroke-width="1.2" fill="none"/></svg></span></a>
</section>

<section class="testimonials">
  <h2 class="head-font">TESTIMONIALS</h2>
  <div class="t-card" style="left:108px">
    <div class="t-badge"><svg width="22" height="18" viewBox="0 0 22 18" fill="#222"><path d="M0 18V10C0 4 3 1 8 0l1 3C6 4 5 6 5 8h4v10zM12 18V10c0-6 3-9 8-10l1 3c-3 1-4 3-4 5h4v10z"/></svg></div>
    <p>Lorem Ipsum is simply dummy text of the printing and typesetting industry lorem Ipsum has been the industry's standard dummy text ever since when centuries, but also the leap into electronic typesetting, remaining essentially &nbsp;sheets containing Lorem Ipsum passages, and more recently with desktop</p>
    <div class="t-avatar" style="background:#c9b8a6" role="img" aria-label="Portrait photo of Dorian Vale"></div>
    <div class="t-name">Dorian Vale</div><div class="t-place">Fernhollow, CA</div>
  </div>
  <div class="t-card" style="left:445px">
    <div class="t-badge"><svg width="22" height="18" viewBox="0 0 22 18" fill="#222"><path d="M0 18V10C0 4 3 1 8 0l1 3C6 4 5 6 5 8h4v10zM12 18V10c0-6 3-9 8-10l1 3c-3 1-4 3-4 5h4v10z"/></svg></div>
    <p>Lorem Ipsum is simply dummy text of the printing and typesetting industry lorem Ipsum has been the industry's standard dummy text ever since when centuries, but also the leap into electronic typesetting, remaining essentially &nbsp;sheets containing Lorem Ipsum passages, and more recently with desktop</p>
    <div class="t-avatar" style="background:#b97a64" role="img" aria-label="Portrait photo of Mira Ostrand"></div>
    <div class="t-name">Mira Ostrand</div><div class="t-place">Ashby, MI</div>
  </div>
  <div class="t-card" style="left:782px">
    <div class="t-badge"><svg width="22" height="18" viewBox="0 0 22 18" fill="#222"><path d="M0 18V10C0 4 3 1 8 0l1 3C6 4 5 6 5 8h4v10zM12 18V10c0-6 3-9 8-10l1 3c-3 1-4 3-4 5h4v10z"/></svg></div>
    <p>Lorem Ipsum is simply dummy text of the printing and typesetting industry lorem Ipsum has been the industry's standard dummy text ever since when centuries, but also the leap into electronic typesetting, remaining essentially &nbsp;sheets containing Lorem Ipsum passages, and more recently with desktop</p>
    <div class="t-avatar" style="background:#44536a" role="img" aria-label="Portrait photo of Tobias Renk"></div>
    <div class="t-name">Tobias Renk</div><div class="t-place">Kettle Cove, ME</div>
  </div>
</section>

<section class="faq">
  <div class="eyebrow">FAQ</div>
  <h2 class="head-font">let’s build something<br>together</h2>
  <p class="text">Lorem Ipsum is simply dummy text of the printing and typesetting industry lorem Ipsum has been the industry's standard dummy text ever since when centuries, but also the leap into electronic typesetting, remaining essentially sheets containing Lorem Ipsum passages, and more recently with desktop</p>
  <a class="btn btn-yellow">Contact Us <span class="dot"><svg viewBox="0 0 6 6"><path d="M2 1l2 2-2 2" stroke="#fdb913" stroke-width="1.2" fill="none"/></svg></span></a>
  <div class="faq-list">
    <div class="faq-item">Lorem Ipsum is simply dummy text printing typesetting industry <b>+</b></div>
    <div class="faq-item">Lorem Ipsum is simply dummy text printing typesetting industry <b>+</b></div>
    <div class="faq-item">Lorem Ipsum is simply dummy text printing typesetting industry <b>+</b></div>
    <div class="faq-item">Lorem Ipsum is simply dummy text printing typesetting industry <b>+</b></div>
    <div class="faq-item">Lorem Ipsum is simply dummy text printing typesetting industry <b>+</b></div>
  </div>
</section>

<section class="partners">
  <div class="partner" style="left:110px;font-size:18px">QUVIRO</div>
  <div class="partner" style="left:280px"><i></i>halvorn</div>
  <div class="partner" style="left:458px"><i></i>plindrex</div>
  <div class="partner" style="left:642px">ZENTRAMO</div>
  <div class="partner" style="left:848px"><i></i>VESKARI</div>
  <div class="seal"></div>
</section>

<footer class="site-footer">
  <div class="foot-brand">Corvella</div>
  <div class="foot-phone-icon"><svg width="24" height="24" viewBox="0 0 24 24" fill="none" stroke="#333" stroke-width="1.8"><path d="M5 3h4l2 5-3 2a12 12 0 0 0 6 6l2-3 5 2v4a2 2 0 0 1-2 2A18 18 0 0 1 3 5a2 2 0 0 1 2-2z"/></svg></div>
  <div class="foot-ask">Call To Ask Any Question</div>
  <div class="foot-num">123-555-0147</div>
  <a class="btn btn-yellow">Get Free Quote <span class="dot"><svg viewBox="0 0 6 6"><path d="M2 1l2 2-2 2" stroke="#fdb913" stroke-width="1.2" fill="none"/></svg></span></a>
  <div class="foot-rule"></div>
  <div class="copyright">Copyright © 2026 corvella-example.com. All rights reserved.</div>
  <div class="socials"><span></span><span></span><span></span><span></span></div>
</footer>

</body>
</html>
```